Math Word Problems Make Your Palms Sweat??

I need a landing page for lead magnet download and email capture. Prospects will get here from QL ad. Landing page should be clean, simple and aimed at parents of Algebra 1 students. I will attach logo. Please use logo brand colors and fonts. The final design should be clear, easy to understand with struggling students and parents that don't know how to help. Copy should include: (lead magnet download info:) Number Story Rescue Pack with examples AND solutions, Conquer word problems with a step by step guide written by former teacher and full time math tutor.

Target Market(s)

Parents of struggling high school math/Algebra 1 students

Colors
33b8a4
ffffff

Requirements
Must have
• address pain points of:
struggling students
word problems causing angst
parents not knowing how to help their child

be clean, simple and easy to see what my message is via copy, images and feel of page

brand colors (ffffff, 5f5e60, 00a99d)and fonts (questrial, glacial indifference and arimo) from attached logo

clear call to action (download the pdf/lead magnet)
Nice to have
• bulleted points, not too wordy but clear message

related images/teens/struggling with math

my headshot if it looks appropriate on page

(I will likely have revisions once I see the first draft)
Should not have
• crowded
hard to read
message hard to decipher
busy
unclear call to action

```html
<!DOCTYPE html>
<html lang="en">
<head>
<meta charset="utf-8">
<title>Clearpath Tutoring – Number Story Rescue Pack</title>
<link href="https://fonts.googleapis.com/css2?family=Poppins:wght@300;400;500;600;700;800&family=Questrial&display=swap" rel="stylesheet">
<style>
:root{
  --teal:#36b795;
  --teal-dark:#2fa585;
  --slate:#555457;
  --ink:#333235;
  --navy:#1b2945;
  --mist:#ebebeb;
  --night:#1c1c1e;
  --white:#ffffff;
  --line:#c9c9c9;
}
*{box-sizing:border-box;margin:0;padding:0}
html,body{width:1200px;height:3721px;overflow:hidden}
body{font-family:'Poppins',sans-serif;color:var(--ink);background:var(--white);position:relative}
.abs{position:absolute}

/* header */
.site-header{position:absolute;left:0;top:0;width:1200px;height:110px;background:var(--white)}
.brand{left:131px;top:24px;display:flex;align-items:center;gap:10px;font-family:'Questrial',sans-serif;font-size:30px;color:var(--teal)}
.brand-mark{width:22px;height:22px;border:3px solid var(--teal)}
.call{left:780px;top:18px;display:flex;align-items:center;gap:10px}
.call small{display:block;font-size:10px;font-weight:600;color:var(--ink)}
.call b{font-size:14px;font-weight:600;color:var(--teal)}
.social-top{left:962px;top:21px;display:flex;gap:12px}
.dot-ring{width:27px;height:27px;border:2px solid var(--teal);border-radius:50%}
.nav{left:557px;top:70px;display:flex;gap:33px;font-size:15px;font-weight:600;color:var(--ink)}

/* hero */
.hero{left:0;top:110px;width:1200px;height:644px;background:radial-gradient(ellipse at 45% 35%,#d9a48a 0%,#b77a64 25%,#8c5d55 50%,#6b6a72 75%,#53606a 100%)}
.hero-arrow{top:286px;width:62px;height:62px;border:3px solid var(--white);border-radius:50%}
.hero-title{left:0;top:335px;width:1200px;text-align:center;font-weight:800;font-size:42px;line-height:60px;color:var(--white);text-transform:uppercase;text-shadow:0 2px 6px rgba(0,0,0,.35)}
.btn-solid{background:var(--teal);color:var(--white);font-weight:600;border-radius:30px;display:flex;align-items:center;justify-content:center}
.hero-btn{left:528px;top:473px;width:197px;height:52px;font-size:19px}
.hero-dots{left:563px;top:572px;display:flex;gap:9px}
.hero-dots span{width:18px;height:18px;border:2px solid var(--white);border-radius:50%}
.hero-dots .on{background:var(--teal);border-color:var(--white)}

/* about */
.about-frame{left:147px;top:862px;width:427px;height:247px;border:5px solid var(--teal)}
.about-photo{left:191px;top:901px;width:383px;height:254px;background:linear-gradient(135deg,#d9d6d2,#bdb6ae 55%,#9c9189)}
.about-title{left:634px;top:868px;font-size:40px;font-weight:800;color:var(--navy)}
.about-title span{color:var(--teal)}
.about-text{left:634px;top:938px;width:440px;font-size:15px;line-height:25px;color:var(--slate)}
.about-text p+p{margin-top:18px}
.btn-ghost{border:3px solid var(--slate);color:var(--teal);font-weight:500;border-radius:30px;display:flex;align-items:center;justify-content:center;background:var(--white)}
.about-btn{left:630px;top:1098px;width:168px;height:48px;font-size:16px}

/* solutions */
.solutions{left:0;top:1282px;width:1200px;height:548px;background:var(--mist)}
.section-title{width:1200px;text-align:center;font-weight:800;color:var(--slate)}
.section-title span{color:var(--teal)}
.sol-title{left:0;top:80px;font-size:50px}
.octagon{top:195px;width:249px;height:249px;background:var(--slate);clip-path:polygon(29% 0,71% 0,100% 29%,100% 71%,71% 100%,29% 100%,0 71%,0 29%);display:flex;flex-direction:column;align-items:center;color:var(--white);font-size:19px;line-height:26px;text-align:center;padding-top:52px}
.octagon.active{background:var(--teal)}
.octagon p{margin:14px 0 12px;letter-spacing:-.3px}

/* why */
.why-photo{left:0;top:1830px;width:1200px;height:480px;background:linear-gradient(90deg,#e3e6e4 0%,#c6d3cf 30%,#3f7b74 55%,#2d6a64 100%)}
.why-card{left:326px;top:1904px;width:531px;height:338px;background:rgba(255,255,255,.82);padding:40px 50px}
.why-card h2{font-size:26px;font-weight:500;color:var(--ink);margin-bottom:16px}
.why-card .lead{font-size:15px;line-height:21px;color:var(--ink)}
.why-card .fine{font-size:11px;line-height:20px;color:var(--slate);margin-top:16px}
.why-btn{margin-top:24px;width:160px;height:44px;background:var(--teal);color:var(--white);font-size:15px;display:flex;align-items:center;justify-content:center;gap:6px}
.mini-dot{width:13px;height:13px;border-radius:50%;background:var(--white)}

/* get started */
.started{left:0;top:2270px;width:1200px;height:274px}
.started h2{left:220px;top:86px;font-size:28px;font-weight:600;color:var(--white)}
.started .lead{left:220px;top:136px;font-size:18px;color:var(--white)}
.started .sub{left:220px;top:168px;font-size:15px;color:#e6e6e6}
.call-btn{left:785px;top:119px;width:156px;height:48px;background:var(--white);color:var(--ink);font-size:17px;display:flex;align-items:center;justify-content:center;gap:8px}
.call-btn .mini-dot{background:var(--teal)}

/* features */
.features{left:0;top:2544px;width:1200px;height:353px;background:var(--teal)}
.feature{top:70px;width:240px;text-align:center;color:var(--white)}
.feature .ring{width:94px;height:94px;border:3px solid var(--white);border-radius:50%;margin:0 auto 20px;display:flex;align-items:center;justify-content:center}
.feature h3{font-size:22px;font-weight:400;margin-bottom:12px}
.feature p{font-size:13px;line-height:19px}

/* contact */
.touch-title{left:0;top:2960px;font-size:40px}
.field{width:314px;height:46px;border:2px solid var(--line);font-size:16px;color:var(--slate);padding:11px 18px;background:var(--white)}
.touch-btn{left:516px;top:3256px;width:168px;height:48px;font-size:16px;border-color:var(--teal);color:var(--navy)}

/* footer */
.footer{left:0;top:3386px;width:1200px;height:335px;background:var(--night);color:var(--white)}
.foot-col{top:62px}
.foot-col h4{font-size:19px;font-weight:600;margin-bottom:8px}
.foot-col li{list-style:none;font-size:14px;line-height:27px}
.foot-contact li{display:flex;gap:10px;align-items:flex-start;line-height:19px;margin-bottom:16px}
.social-foot{left:884px;top:194px;display:flex;gap:7px}
.social-foot .dot-ring{width:32px;height:32px}
.foot-rule{left:0;top:267px;width:1200px;height:1px;background:#3a3a3c}
.copyright{left:0;top:294px;width:1200px;text-align:center;font-size:14px;color:#dcdcdc}
</style>
</head>
<body>

<header class="site-header">
  <div class="abs brand"><span class="brand-mark"></span>Clearpath Tutoring</div>
  <div class="abs call">
    <svg width="28" height="28" viewBox="0 0 24 24" fill="none" stroke="#333235" stroke-width="1.6"><path d="M5 3h4l2 5-3 2a11 11 0 0 0 6 6l2-3 5 2v4a2 2 0 0 1-2 2A17 17 0 0 1 3 5a2 2 0 0 1 2-2z"/></svg>
    <div><small>CALL US</small><b>+1 555 014 2200</b></div>
  </div>
  <div class="abs social-top"><span class="dot-ring"></span><span class="dot-ring"></span><span class="dot-ring"></span></div>
  <nav class="abs nav"><span>HOME</span><span>MISSION</span><span>ABOUT US</span><span>PROGRAMS</span><span>CONTACT US</span></nav>
</header>

<section class="abs hero" role="img" aria-label="Photo of smiling high school students in a classroom">
  <svg class="abs hero-arrow" style="left:124px" viewBox="0 0 62 62"><path d="M35 19 23 31l12 12" fill="none" stroke="#fff" stroke-width="4"/></svg>
  <svg class="abs hero-arrow" style="left:1014px" viewBox="0 0 62 62"><path d="M27 19l12 12-12 12" fill="none" stroke="#fff" stroke-width="4"/></svg>
  <h1 class="abs hero-title">Math Word Problems<br>Make Your Palms Sweat</h1>
  <div class="abs btn-solid hero-btn">GET THE PDF</div>
  <div class="abs hero-dots"><span></span><span class="on"></span><span></span></div>
</section>

<section>
  <div class="abs about-frame"></div>
  <div class="abs about-photo" role="img" aria-label="Headshot of the tutor, a former math teacher"></div>
  <h2 class="abs about-title">ABOUT <span>US.......</span></h2>
  <div class="abs about-text">
    <p>Former classroom teacher and full time math tutor, helping Algebra 1 students turn confusion into confidence.</p>
    <p>A clear, step by step method shows your teen how to read, set up and solve any word problem.</p>
  </div>
  <div class="abs btn-ghost about-btn">LEARN MORE</div>
</section>

<section class="abs solutions">
  <h2 class="abs section-title sol-title">OUR <span>SOLUTIONS</span></h2>
  <div class="abs octagon" style="left:203px">
    <svg width="44" height="50" viewBox="0 0 44 50" fill="none" stroke="#fff" stroke-width="2"><circle cx="22" cy="10" r="7"/><path d="M8 44V28l14-8 14 8v16l-14 6z M22 20v30"/></svg>
    <p>Struggling<br>Students</p>
    <svg width="32" height="32" viewBox="0 0 32 32" fill="none" stroke="#fff" stroke-width="2"><circle cx="16" cy="16" r="14"/><path d="M10 13l6 6 6-6"/></svg>
  </div>
  <div class="abs octagon active" style="left:476px">
    <svg width="50" height="50" viewBox="0 0 50 50" fill="none" stroke="#fff" stroke-width="2"><circle cx="25" cy="12" r="7"/><path d="M4 20v14l10 10h8V34L12 24M46 20v14L36 44h-8V34l10-10"/></svg>
    <p>Word Problems<br>Causing Angst</p>
    <svg width="32" height="32" viewBox="0 0 32 32" fill="none" stroke="#fff" stroke-width="2"><circle cx="16" cy="16" r="14"/><path d="M10 13l6 6 6-6"/></svg>
  </div>
  <div class="abs octagon" style="left:749px">
    <svg width="50" height="50" viewBox="0 0 50 50" fill="none" stroke="#fff" stroke-width="2"><circle cx="18" cy="12" r="5"/><circle cx="32" cy="12" r="5"/><circle cx="25" cy="22" r="4"/><path d="M4 22v14l10 10M46 22v14L36 46"/></svg>
    <p>Parents Not Knowing<br>How to Help Their Child</p>
    <svg width="32" height="32" viewBox="0 0 32 32" fill="none" stroke="#fff" stroke-width="2"><circle cx="16" cy="16" r="14"/><path d="M10 13l6 6 6-6"/></svg>
  </div>
</section>

<section>
  <div class="abs why-photo" role="img" aria-label="Photo of a teacher holding a book in front of a chalkboard with math formulas"></div>
  <div class="abs why-card">
    <h2>Why Choose Us?</h2>
    <p class="lead">Get the free Number Story Rescue Pack: real word problem examples AND full solutions, written by a former teacher.</p>
    <p class="fine">Conquer word problems with a step by step guide your teen can follow and you can use to help at home.</p>
    <div class="why-btn">Download PDF <span class="mini-dot"></span></div>
  </div>
</section>

<section class="abs started">
  <svg class="abs" style="left:0;top:0" width="1200" height="274" viewBox="0 0 1200 274"><path d="M0 20Q300 4 600 10T1200 0V274H0z" fill="#555457"/></svg>
  <h2 class="abs">Get Started Today!</h2>
  <p class="abs lead">Download the free Number Story Rescue Pack today!</p>
  <p class="abs sub">Examples and solutions to help your teen, and you, feel sure.</p>
  <div class="abs call-btn">Download <span class="mini-dot"></span></div>
</section>

<section class="abs features">
  <div class="abs feature" style="left:192px">
    <div class="ring"><svg width="48" height="48" viewBox="0 0 48 48" fill="none" stroke="#fff" stroke-width="3"><circle cx="28" cy="20" r="11"/><path d="M20 28 8 40"/></svg></div>
    <h3>Professionalism</h3>
    <p>Written by a former teacher and full time math tutor</p>
  </div>
  <div class="abs feature" style="left:486px">
    <div class="ring"><svg width="48" height="48" viewBox="0 0 48 48" fill="none" stroke="#fff" stroke-width="3"><circle cx="24" cy="24" r="18"/><path d="M15 24l7 7 13-14"/></svg></div>
    <h3>Better Results</h3>
    <p>Step by step practice that builds real Algebra 1 confidence</p>
  </div>
  <div class="abs feature" style="left:767px">
    <div class="ring"><svg width="48" height="48" viewBox="0 0 48 48" fill="none" stroke="#fff" stroke-width="3"><circle cx="12" cy="12" r="3"/><circle cx="36" cy="24" r="3"/><circle cx="12" cy="36" r="3"/><path d="M15 12h15a6 6 0 0 1 0 12H33M33 24H18a6 6 0 0 0 0 12"/></svg></div>
    <h3>Quality Work</h3>
    <p>Worked examples AND solutions so parents can help too</p>
  </div>
</section>

<section>
  <h2 class="abs section-title touch-title">GET IN <span>TOUCH</span></h2>
  <div class="abs field" style="left:273px;top:3028px">Your Name</div>
  <div class="abs field" style="left:273px;top:3100px">Email Address</div>
  <div class="abs field" style="left:273px;top:3172px">Phone</div>
  <div class="abs field" style="left:613px;top:3028px">Subject</div>
  <div class="abs field" style="left:613px;top:3100px;height:118px"></div>
  <div class="abs btn-ghost touch-btn">GET THE PACK</div>
</section>

<footer class="abs footer">
  <div class="abs foot-col" style="left:132px"><h4>QUICK LINKS</h4><ul><li>Home</li><li>About Us</li><li>Mission</li><li>Programs</li><li>Support</li></ul></div>
  <div class="abs foot-col" style="left:351px"><h4>INFORMATIONS</h4><ul><li>Get in Touch</li><li>Why chooses</li><li>Solutions</li><li>Cotact Us</li></ul></div>
  <div class="abs foot-col foot-contact" style="left:567px"><h4>CONTACT US</h4>
    <ul>
      <li><svg width="14" height="18" viewBox="0 0 14 18"><path d="M7 0a7 7 0 0 0-7 7c0 5 7 11 7 11s7-6 7-11a7 7 0 0 0-7-7zm0 10a3 3 0 1 1 0-6 3 3 0 0 1 0 6z" fill="#fff"/></svg><span style="font-size:13px">42 Maple Grove Lane,<br>Austin TX 73301</span></li>
      <li><svg width="16" height="16" viewBox="0 0 24 24" fill="#fff"><path d="M5 3h4l2 5-3 2a11 11 0 0 0 6 6l2-3 5 2v4a2 2 0 0 1-2 2A17 17 0 0 1 3 5a2 2 0 0 1 2-2z"/></svg><span style="font-size:14px">(555) 014 2200</span></li>
      <li><svg width="16" height="12" viewBox="0 0 16 12"><rect width="16" height="12" fill="#fff"/><path d="M0 0l8 7 8-7" fill="none" stroke="#1c1c1e" stroke-width="1.5"/></svg><span style="font-size:14px">hello@clearpathtutor.com</span></li>
    </ul>
  </div>
  <div class="abs social-foot"><span class="dot-ring"></span><span class="dot-ring"></span><span class="dot-ring"></span><span class="dot-ring"></span></div>
  <div class="abs foot-rule"></div>
  <p class="abs copyright">© 2020 Clearpath Tutoring. All Rights are Reserved.</p>
</footer>

</body>
</html>
```